Business Card for my building company

I would like the card to make a statement, so as soon as you see the card you think "wow nice card' and then read the details on the card its self. Also i would like to be able to put in the detail for the MUST HAVES so please Crete a box that i can alter depending on who in my business needs the cards. Thank you

Target Market(s)

Any one looking to build a house/ townhouse or duplex

Industry/Entity Type

Home Builder

Contact Information for Business Card

I would like the card to have the logo on the card and the must haves

Font styles to use
Sans Serif

Requirements
Must have
• Name
• Phone Number
• Email Address
• Website
• Licence Number
• Abn

```html
<!DOCTYPE html>
<html lang="en">
<head>
<meta charset="utf-8">
<title>Stonebridge Builders – Business Card</title>
<link href="https://fonts.googleapis.com/css2?family=Open+Sans:wght@400;600;700;800&display=swap" rel="stylesheet">
<style>
  :root {
    --backdrop: #3b322e;
    --card: #ffffff;
    --ink: #1c1c1c;
    --gold: #b8913e;
    --gold-dark: #9c7a2e;
  }
  * { box-sizing: border-box; margin: 0; padding: 0; }
  html, body {
    width: 1200px;
    height: 844px;
    overflow: hidden;
    background: var(--backdrop);
    font-family: "Open Sans", Arial, sans-serif;
  }
  .stage {
    position: relative;
    width: 1200px;
    height: 844px;
  }
  .card {
    position: absolute;
    top: 263px;
    width: 520px;
    height: 318px;
    background: var(--card);
    box-shadow: 0 10px 24px rgba(0,0,0,0.35);
  }
  .card--front { left: 60px; }
  .card--back  { left: 620px; }

  .brand {
    position: absolute;
    display: flex;
    align-items: center;
    gap: 10px;
    white-space: nowrap;
  }
  .brand__mark {
    width: 22px;
    height: 22px;
    background: var(--gold);
    flex: none;
  }
  .brand__name {
    font-weight: 800;
    font-size: 26px;
    color: var(--ink);
    letter-spacing: 0.5px;
  }
  .card--front .brand { left: 118px; top: 92px; }
  .card--back .brand  { left: 50%; top: 50%; transform: translate(-50%, -50%); }

  .contact {
    position: absolute;
    right: 28px;
    top: 150px;
    list-style: none;
    text-align: right;
  }
  .contact__item {
    display: flex;
    justify-content: flex-end;
    align-items: center;
    gap: 7px;
    font-size: 13px;
    line-height: 23px;
    color: var(--ink);
  }
  .contact__icon {
    width: 11px;
    height: 11px;
    flex: none;
  }

  .holder {
    position: absolute;
    left: 34px;
    bottom: 34px;
  }
  .holder__name {
    font-weight: 600;
    font-size: 19px;
    color: var(--gold);
    margin-bottom: 4px;
  }
  .holder__detail {
    font-size: 14px;
    line-height: 23px;
    color: var(--ink);
  }
  .holder__label {
    font-weight: 600;
    color: var(--gold);
  }
</style>
</head>
<body>
<main class="stage">

  <section class="card card--front" aria-label="Business card front">
    <div class="brand">
      <span class="brand__mark"></span>
      <span class="brand__name">Stonebridge Builders</span>
    </div>

    <ul class="contact">
      <li class="contact__item">
        <span>(044)-555-0182</span>
        <svg class="contact__icon" viewBox="0 0 12 12" aria-hidden="true">
          <path d="M2.5 1 L4.5 1 L5.3 3.4 L4 4.4 C4.7 5.9 6 7.2 7.6 8 L8.6 6.7 L11 7.5 L11 9.5 C11 10.3 10.3 11 9.5 11 C5 11 1 7 1 2.5 C1 1.7 1.7 1 2.5 1 Z" fill="var(--gold)"/>
        </svg>
      </li>
      <li class="contact__item">
        <span>info@stonebridgebuild.com</span>
        <svg class="contact__icon" viewBox="0 0 12 12" aria-hidden="true">
          <rect x="0.5" y="2.5" width="11" height="7.5" fill="var(--gold)"/>
          <path d="M0.5 2.5 L6 7 L11.5 2.5" fill="none" stroke="#fff" stroke-width="1"/>
        </svg>
      </li>
      <li class="contact__item">
        <span>www.stonebridgebuild.com</span>
        <svg class="contact__icon" viewBox="0 0 12 12" aria-hidden="true">
          <circle cx="6" cy="6" r="5.5" fill="var(--gold)"/>
          <path d="M0.5 6 H11.5 M6 0.5 C3.5 3 3.5 9 6 11.5 M6 0.5 C8.5 3 8.5 9 6 11.5" fill="none" stroke="#fff" stroke-width="0.8"/>
        </svg>
      </li>
    </ul>

    <div class="holder">
      <p class="holder__name">Daniel Harper</p>
      <p class="holder__detail"><span class="holder__label">Licence Number :</span> 123 456 789</p>
      <p class="holder__detail"><span class="holder__label">Abn :</span> 123 456 789</p>
    </div>
  </section>

  <section class="card card--back" aria-label="Business card back">
    <div class="brand">
      <span class="brand__mark"></span>
      <span class="brand__name">Stonebridge Builders</span>
    </div>
  </section>

</main>
</body>
</html>
```